marble ridge yard works
cards+letter head+envelopes+signs
marble ridge yard works -
Creative Brief
Use specific fonts
you deside
Simple
Lou Kettering
owner/operator
42 willow ave w po box 953 st.jacobs, on n0b 2n0
lou@marbleridge-example.ca
www.marbleridge-example.ca
professional member of greenscape guild. (they have a logo for this)
plain or watermark my log or just my brand mark.

```html
<!DOCTYPE html>
<html lang="en">
<head>
<meta charset="utf-8">
<title>Marble Ridge Yard Works – Stationery Set</title>
<link href="https://fonts.googleapis.com/css2?family=Lato:wght@400;700;900&display=swap" rel="stylesheet">
<style>
  :root{
    --green:#3f9b3a;
    --green-light:#7cc36a;
    --green-dark:#1f6b2a;
    --ink:#333;
    --grey:#8a8a8a;
    --rule:#c9c9c9;
    --paper:#fff;
    --bg:#fff;
  }
  *{box-sizing:border-box;margin:0;padding:0}
  html,body{width:1200px;height:518px;overflow:hidden;background:var(--bg);font-family:'Lato',sans-serif;color:var(--ink)}
  .canvas{position:relative;width:1200px;height:518px}
  .sheet{position:absolute;background:var(--paper);box-shadow:0 0 3px rgba(0,0,0,.25);overflow:hidden}
  .tab{position:absolute;top:0;left:0;background:var(--green-dark);color:#fff;font-size:6px;letter-spacing:.5px;padding:2px 6px;text-transform:lowercase}
  .brand{position:absolute;display:flex;align-items:center;gap:4px;font-weight:900;color:var(--green-dark);text-transform:uppercase;line-height:1;white-space:nowrap}
  .brand .dot{width:9px;height:9px;border-radius:50%;background:var(--green);flex:none}
  .swoosh{position:absolute;left:0;bottom:0;width:100%}
  .footer-text{position:absolute;font-size:5px;color:#fff;line-height:1.5;white-space:nowrap}

  /* invoice */
  .invoice{left:7px;top:7px;width:348px;height:502px}
  .invoice .brand{left:22px;top:42px;font-size:12px}
  .field-row{position:absolute;left:22px;right:22px;top:78px;display:flex;gap:10px;font-size:5.5px}
  .field-row span{flex:1;border-bottom:1px solid var(--rule);padding-bottom:2px}
  .box{position:absolute;border:1px solid var(--rule);font-size:5px;padding:3px;line-height:2.2;color:var(--grey)}
  .details-title{position:absolute;left:22px;right:22px;top:158px;text-align:center;font-size:6px;font-weight:700;color:var(--green-dark)}
  .table{position:absolute;left:22px;right:22px;top:168px;height:200px;border:1px solid var(--rule);display:grid;grid-template-columns:28px 1fr 60px}
  .table div{border-right:1px solid var(--rule);font-size:5px;color:var(--grey);padding:2px;background:repeating-linear-gradient(to bottom,transparent 0 11px,#e4e4e4 11px 12px)}
  .table div:last-child{border-right:none}
  .notes{left:22px;top:376px;width:200px;height:34px;line-height:1.4}
  .total{left:260px;top:376px;width:66px;height:14px;line-height:1.4}

  /* letterhead */
  .letterhead{left:379px;top:7px;width:348px;height:502px}
  .letterhead .brand{left:22px;top:42px;font-size:12px}

  /* cards */
  .card{position:absolute;left:751px;width:102px;height:52px;background:var(--paper);box-shadow:0 0 3px rgba(0,0,0,.3);overflow:hidden}
  .card-front{top:216px}
  .card-back{top:274px}
  .card .brand{font-size:5.5px;gap:2px}
  .card .brand .dot{width:5px;height:5px}
  .card-front .brand{left:5px;top:6px}
  .card-back .brand{left:5px;top:8px}
  .card-name{position:absolute;left:5px;top:26px;font-size:4.5px;line-height:1.3}
  .card-name strong{color:var(--green-dark)}
  .card-web{position:absolute;left:5px;bottom:6px;font-size:4px;color:var(--grey)}
  .card-band{position:absolute;right:0;top:0;width:14px;height:100%;background:linear-gradient(var(--green-light),var(--green-dark))}

  /* envelopes */
  .envelope{width:324px;height:216px}
  .env-top{left:869px;top:10px}
  .env-bottom{left:869px;top:290px;height:219px}
  .envelope .brand{left:18px;top:30px;font-size:11px}
  .env-address{position:absolute;left:58px;top:56px;font-size:5px;color:var(--grey);white-space:nowrap}
  .env-band{position:absolute;right:0;top:0;width:30px;height:100%;background:linear-gradient(var(--green-light),var(--green-dark));display:flex;align-items:center;justify-content:center}
  .env-band span{transform:rotate(90deg);color:#fff;font-size:6px;white-space:nowrap;letter-spacing:.5px}
  .complements{position:absolute;right:40px;bottom:22px;color:#fff;font-size:12px;white-space:nowrap}
  .window{position:absolute;left:110px;top:110px;width:120px;height:40px;border:1px solid #e3e3e3;border-radius:3px}
</style>
</head>
<body>
<main class="canvas">

  <section class="sheet invoice" aria-label="Invoice">
    <div class="tab">invoice</div>
    <div class="brand"><span class="dot"></span>Marble Ridge Yard Works</div>
    <div class="field-row"><span>Invoice No.</span><span>Date</span><span>Phone</span></div>
    <div class="box" style="left:22px;top:92px;width:110px;height:52px">Bill To<br>Contact<br>Phone</div>
    <div class="box" style="left:142px;top:92px;width:120px;height:14px;line-height:1.4">Ship To</div>
    <div class="details-title">Invoice Details</div>
    <div class="table"><div>Qty</div><div>Description</div><div>Amount</div></div>
    <div class="box notes">Notes</div>
    <div class="box total">Total</div>
    <svg class="swoosh" viewBox="0 0 348 90" preserveAspectRatio="none" height="90">
      <defs><linearGradient id="g1" x1="0" x2="1"><stop offset="0" stop-color="#1f6b2a"/><stop offset="1" stop-color="#7cc36a"/></linearGradient></defs>
      <path d="M0 40 C90 10 200 70 348 22 L348 90 L0 90Z" fill="url(#g1)"/>
      <path d="M0 34 C90 4 200 64 348 16" fill="none" stroke="#555" stroke-width="3"/>
    </svg>
    <p class="footer-text" style="left:14px;bottom:10px">42 willow ave w po box 953<br>fernbrook, on x0x 9z9</p>
    <p class="footer-text" style="right:14px;bottom:10px;text-align:right">Tel 555 010 0142<br>www.marbleridge-example.ca</p>
  </section>

  <section class="sheet letterhead" aria-label="Letterhead">
    <div class="tab">letterhead</div>
    <div class="brand"><span class="dot"></span>Marble Ridge Yard Works</div>
    <svg class="swoosh" viewBox="0 0 348 90" preserveAspectRatio="none" height="90">
      <defs><linearGradient id="g2" x1="0" x2="1"><stop offset="0" stop-color="#1f6b2a"/><stop offset="1" stop-color="#7cc36a"/></linearGradient></defs>
      <path d="M0 40 C90 10 200 70 348 22 L348 90 L0 90Z" fill="url(#g2)"/>
      <path d="M0 34 C90 4 200 64 348 16" fill="none" stroke="#555" stroke-width="3"/>
    </svg>
    <p class="footer-text" style="left:14px;bottom:10px">42 willow ave w po box 953<br>fernbrook, on x0x 9z9</p>
    <p class="footer-text" style="right:14px;bottom:10px;text-align:right">lou@marbleridge-example.ca<br>www.marbleridge-example.ca</p>
  </section>

  <article class="card card-front" aria-label="Business card front">
    <div class="brand"><span class="dot"></span>Marble Ridge</div>
    <p class="card-name"><strong>Lou Kettering</strong><br>owner/operator</p>
    <div class="card-band"></div>
  </article>
  <article class="card card-back" aria-label="Business card back">
    <div class="brand"><span class="dot"></span>Marble Ridge Yard Works</div>
    <p class="card-web">www.marbleridge-example.ca</p>
  </article>

  <section class="sheet envelope env-top" aria-label="Envelope">
    <div class="brand"><span class="dot"></span>Marble Ridge</div>
    <p class="env-address">42 willow ave w, fernbrook, on x0x 9z9</p>
    <svg style="position:absolute;right:30px;top:0" width="120" height="40" viewBox="0 0 120 40">
      <path d="M0 0 C40 10 80 30 120 22 L120 0Z" fill="#3f9b3a"/>
    </svg>
    <div class="window"></div>
    <div class="env-band"><span>envelope</span></div>
  </section>

  <section class="sheet envelope env-bottom" aria-label="Compliments envelope">
    <div class="brand"><span class="dot"></span>Marble Ridge</div>
    <p class="env-address">42 willow ave w, fernbrook, on x0x 9z9</p>
    <div class="env-band" style="height:130px"><span>compliments</span></div>
    <svg class="swoosh" viewBox="0 0 324 110" preserveAspectRatio="none" height="110">
      <defs><linearGradient id="g3" x1="0" x2="1"><stop offset="0" stop-color="#7cc36a"/><stop offset="1" stop-color="#1f6b2a"/></linearGradient></defs>
      <path d="M40 110 C120 90 220 40 324 20 L324 110Z" fill="url(#g3)"/>
    </svg>
    <p class="complements">with complements</p>
  </section>

</main>
</body>
</html>
```